Lumawerks Business Card Design

I need a business card design for a new Business, that is focused on Custom Made Designer Furniture. that is aimed at the mid to high end markets. I would like a card that would in some way portray what I do for my clients in the way we are able to make any idea a reality and also work within a set budget to meet their requirements.
I like quite contemporary colours and styling and I want the final design to communicate a Contemporary and Professional image.

Target Market(s)

mid to high end market

Industry/Entity Type

Business

Contact Information for Business Card

Lumawerks
Darren Holtzmann
18 Wexbury Rd, Kelston, Auckland, New Zealand 0712.

Requirements
Nice to have
• I would also like to utilize the spot gloss or raised print on my cards

```html
<!DOCTYPE html>
<html lang="en">
<head>
<meta charset="utf-8">
<title>Lumawerks Business Card</title>
<link rel="stylesheet" href="https://fonts.googleapis.com/css2?family=Michroma&family=Open+Sans:wght@400&display=swap">
<style>
  :root {
    --page-bg: #e6e6e7;
    --card-white: #fbfbfb;
    --card-charcoal: #5a5a5c;
    --name-blue: #1f5fa8;
    --ink-dark: #2a2a2a;
    --ink-grey: #7d7d7d;
    --ink-light: #b4b4b6;
  }
  * { box-sizing: border-box; margin: 0; padding: 0; }
  html, body { width: 1200px; height: 883px; overflow: hidden; }
  body {
    background: var(--page-bg);
    display: flex;
    align-items: center;
    justify-content: center;
    gap: 50px;
    font-family: "Michroma", "Open Sans", sans-serif;
  }
  .card {
    position: relative;
    width: 520px;
    height: 297px;
    border-radius: 30px;
    box-shadow: 0 10px 26px rgba(0,0,0,.16);
    overflow: hidden;
  }
  .card--front { background: var(--card-white); }
  .card--back {
    background: var(--card-charcoal);
    display: flex;
    align-items: center;
    justify-content: center;
  }
  .brand { display: flex; flex-direction: column; }
  .brand__name {
    font-family: "Michroma", sans-serif;
    font-weight: 400;
    letter-spacing: 1px;
    line-height: 1;
  }
  .brand__slogan {
    font-family: "Open Sans", sans-serif;
    margin-top: 7px;
    line-height: 1;
  }
  .card--front .brand {
    position: absolute;
    left: 26px;
    top: 44px;
  }
  .card--front .brand__name { font-size: 25px; color: var(--ink-grey); }
  .card--front .brand__slogan { font-size: 13.5px; color: var(--ink-grey); }
  .card--back .brand__name { font-size: 28px; color: var(--ink-light); }
  .card--back .brand__slogan { font-size: 15px; color: var(--ink-light); }

  .holder {
    position: absolute;
    right: 26px;
    top: 126px;
    text-align: right;
  }
  .holder__name {
    font-size: 13px;
    color: var(--name-blue);
    letter-spacing: .5px;
  }
  .holder__title {
    font-size: 8.5px;
    color: var(--ink-dark);
    margin-top: 4px;
  }
  .contact {
    position: absolute;
    left: 26px;
    top: 158px;
    font-size: 7px;
    color: var(--ink-dark);
    list-style: none;
    line-height: 1;
  }
  .contact__address { line-height: 1.55; margin-bottom: 9px; width: 200px; }
  .contact__item { display: flex; align-items: center; gap: 6px; margin-bottom: 7px; }
  .contact__item svg { width: 9px; height: 9px; flex: none; }
</style>
</head>
<body>
  <section class="card card--front" aria-label="Card front">
    <div class="brand">
      <span class="brand__name">Lumawerks</span>
      <span class="brand__slogan">Sample Slogan Goes Here</span>
    </div>

    <div class="holder">
      <p class="holder__name">DARREN HOLTZMANN</p>
      <p class="holder__title">Managing Director</p>
    </div>

    <ul class="contact">
      <li class="contact__address">18 Wexbury Rd, Kelston, Auckland,<br>New Zealand 0712</li>
      <li class="contact__item">
        <svg viewBox="0 0 10 10"><path d="M2 1 L3.5 1 L4.2 3 L3.2 3.8 Q4 5.8 6.2 6.8 L7 5.8 L9 6.5 L9 8 Q8.5 9 7.5 9 Q2 8 1 2.5 Q1 1.3 2 1 Z" fill="var(--ink-dark)"/></svg>
        <span>09 412 7730</span>
      </li>
      <li class="contact__item">
        <svg viewBox="0 0 10 10"><rect x="2.5" y=".5" width="5" height="9" rx="1" fill="none" stroke="var(--ink-dark)"/><circle cx="5" cy="8" r=".5" fill="var(--ink-dark)"/></svg>
        <span>021 568 2094</span>
      </li>
      <li class="contact__item">
        <svg viewBox="0 0 10 10"><rect x="1" y="4" width="8" height="5" fill="var(--ink-dark)"/><rect x="3" y="1" width="4" height="3" fill="none" stroke="var(--ink-dark)" stroke-width=".8"/></svg>
        <span>09 412 7731</span>
      </li>
      <li class="contact__item">
        <svg viewBox="0 0 10 10"><rect x=".5" y="2" width="9" height="6" fill="var(--ink-dark)"/><path d="M.5 2 L5 5.5 L9.5 2" fill="none" stroke="var(--card-white)" stroke-width=".7"/></svg>
        <span>darren@lumawerks.co.nz</span>
      </li>
      <li class="contact__item">
        <svg viewBox="0 0 10 10"><circle cx="5" cy="5" r="4.3" fill="none" stroke="var(--ink-dark)" stroke-width=".9"/><ellipse cx="5" cy="5" rx="1.8" ry="4.3" fill="none" stroke="var(--ink-dark)" stroke-width=".7"/><path d="M.7 5 H9.3" stroke="var(--ink-dark)" stroke-width=".7"/></svg>
        <span>www.lumawerks.co.nz</span>
      </li>
    </ul>
  </section>

  <section class="card card--back" aria-label="Card back">
    <div class="brand">
      <span class="brand__name">Lumawerks</span>
      <span class="brand__slogan">Sample Slogan Goes Here</span>
    </div>
  </section>
</body>
</html>
```